Web Design Business Card

I need a new business card designed, we recently rebranded and I need to get a fresh design to match our new logo, colours and branding.

Details:

Dorian Keeble | Founder & CEO
Address: 7 Fernhollow Lane, #04-09 Maplecrest Vale, Singapore 583104
Tel: +65 93468120
Web: www.plumtrove.com.sg
hello@plumtrove.com.sg

I've attached my old card as well

Requirements
Must have
• Front and Back
Interesting use of logo
Correct use of colour scheme

```html
<!DOCTYPE html>
<html lang="en">
<head>
<meta charset="utf-8">
<title>Plumtrove Business Card – Back and Front</title>
<link rel="stylesheet" href="https://fonts.googleapis.com/css2?family=Montserrat:wght@400;500;600;700&display=swap">
<style>
  :root {
    --backdrop: #e9e7e4;
    --taupe: #6f6259;
    --paper: #ffffff;
    --sky: #3fb6ec;
    --sky-light: #7fd3f7;
    --ink-brown: #6a5d55;
    --text-light: #ffffff;
  }
  * { margin: 0; padding: 0; box-sizing: border-box; }
  html, body {
    width: 1200px;
    height: 1000px;
    overflow: hidden;
    background: var(--backdrop);
    font-family: "Montserrat", sans-serif;
  }
  .canvas {
    position: relative;
    width: 1200px;
    height: 1000px;
  }
  .card {
    position: absolute;
    left: 250px;
    width: 700px;
    height: 400px;
    filter: drop-shadow(0 6px 14px rgba(0,0,0,0.18));
  }
  .card--back { top: 60px; }
  .card--front { top: 540px; }
  .card-shape {
    position: absolute;
    inset: 0;
    width: 700px;
    height: 400px;
  }
  .card-shape--taupe { fill: var(--taupe); }
  .card-shape--paper { fill: var(--paper); }

  /* Back: contact side */
  .brand-dot {
    position: absolute;
    border-radius: 50%;
    background: linear-gradient(160deg, var(--sky) 0%, var(--sky-light) 100%);
  }
  .card--back .brand-dot {
    left: 70px;
    top: 88px;
    width: 84px;
    height: 84px;
  }
  .holder {
    position: absolute;
    left: 186px;
    top: 78px;
    color: var(--text-light);
  }
  .holder-name {
    font-size: 50px;
    font-weight: 600;
    letter-spacing: 0.5px;
    text-transform: lowercase;
    line-height: 1;
  }
  .holder-role {
    margin-top: 8px;
    font-size: 15px;
    font-weight: 500;
    letter-spacing: 1px;
    color: var(--sky);
    text-transform: uppercase;
  }
  .contact {
    position: absolute;
    left: 186px;
    top: 180px;
    color: var(--text-light);
    font-size: 17px;
    font-weight: 500;
    letter-spacing: 1px;
    list-style: none;
  }
  .contact-address { line-height: 1.3; margin-bottom: 14px; }
  .contact-line { margin-bottom: 12px; }

  /* Front: brand side */
  .card--front .brand-dot {
    left: 150px;
    top: 128px;
    width: 130px;
    height: 130px;
  }
  .brand {
    position: absolute;
    left: 300px;
    top: 150px;
  }
  .brand-name {
    font-size: 64px;
    font-weight: 700;
    color: var(--ink-brown);
    line-height: 1;
    letter-spacing: -0.5px;
  }
  .brand-tagline {
    margin-top: 10px;
    font-size: 17px;
    font-weight: 600;
    letter-spacing: 2.4px;
    color: var(--sky);
    text-transform: uppercase;
  }
</style>
</head>
<body>
<main class="canvas">
  <section class="card card--back" aria-label="Business card back with contact details">
    <svg class="card-shape card-shape--taupe" viewBox="0 0 700 400" aria-hidden="true">
      <path d="M0 0 H500 A200 200 0 0 1 700 200 V400 H0 Z"/>
    </svg>
    <span class="brand-dot" aria-hidden="true"></span>
    <div class="holder">
      <h1 class="holder-name">Dorian Keeble</h1>
      <p class="holder-role">Founder &amp; CEO</p>
    </div>
    <ul class="contact">
      <li class="contact-address">7 Fernhollow Lane<br>#04-09 Maplecrest Vale<br>Singapore 583104</li>
      <li class="contact-line">+65 93468120</li>
      <li class="contact-line">www.plumtrove.com.sg</li>
      <li class="contact-line">hello@plumtrove.com.sg</li>
    </ul>
  </section>

  <section class="card card--front" aria-label="Business card front with brand name">
    <svg class="card-shape card-shape--paper" viewBox="0 0 700 400" aria-hidden="true">
      <path d="M150 0 H700 V400 H0 V290 A70 70 0 0 0 0 150 A150 150 0 0 1 150 0 Z"/>
    </svg>
    <span class="brand-dot" aria-hidden="true"></span>
    <div class="brand">
      <h2 class="brand-name">plumtrove</h2>
      <p class="brand-tagline">Web Design &amp; Consultancy</p>
    </div>
  </section>
</main>
</body>
</html>
```